Lotvantage.com Webpage Design

Design Brief for lotvantage.com (Copy of Brief also in attached Word file)

Name of Website- lotvantage.com (existing logo and look & feel of website to be changed)

Logo - Finalised. The logo files are attached with the brief as “logo.jpeg”. The “Blue- Grey” version of the logo is for use on lighter backgrounds and the “Orange-White” version of the logo is for use on darker backgrounds. (A full Black version of the logo is also attached). Both versions may be used in different parts of the website. All attached files are in .png format.
Status - The website in functional and is undergoing user trials. However, we want to improve the look & feel of the website so at it seems
a. cotemporary,
b. Easy to Navigate
c. professional and
d. Vibrant.

Please visit ‘lotvantage.com’ to check out the website and its functionalities – please use it only as a reference for the features & functions to be provided, however the designer should use a ‘Free Hand’ in designing the composition of various parts of the webpage without getting too influenced by the existing design

Objective of the Website ‘lotvantage.com –
a. It is a portal focussed on listing of ‘Retail’ specific real-estate properties by developers, owners and realty brokers. The properties shall listed under the following four categories-
i. Retail Malls
ii. Shopping Complexes
iii. High-street shops
iv. Retail Warehouses
*refer lotvantage.com for better clarity

b. The abovementioned properties shall be listed either for ‘Sale’ or ‘rent\lease’ or both

c. Users shall visit the site in case they wish to acquire a retail \ shop space either on ‘sale’ or ‘rent’. These Users would be able to specify the ‘Search Criteria’ through the tool-bars provided on the website – the ‘Search Criteria’ shall comprise of ‘Type of space category’, ‘City’, ‘Locality’, transaction type ie ‘Rent \ Sale’ and ‘Area Range’

d. The main revenue model for the website shall be listing fee ( or advertising charges ) payable by those listing their properties on the website.

Three Main Pages of Website (lotvantage.com) that need to be designed -
a. Main Home Page (visit the web link - http://lotvantage.com/ ) - The main home page has the “Search Toolbar” for specifying of Search Criteria by the User. It shall also have the following features & functions-
i. Main Advertising Banner
ii. Featured Projects
iii. New Launches
iv. Toolbar with buttons – ‘Advertise with Us’, ‘Listings Alert’, ‘Lot Mavens’, ‘Advertiser Login’

b. Property Listings Page (visit the web link - http://lotvantage.com/gurgaon-in-india ) - The List of property options that match the Criteria specified by the ‘User’ get displayed on this page.

c. Property Detail Page - When the ‘User’ clicks on the “More….” Button on the ‘Property Listings Page’ (given in point b. above) the web page with the details of the property opens. (For Example – visit the web link - http://lotvantage.com/brevo-Shopping-Complex-brevo-quadrel-gurgaon-636 )

Note:- Please refer to attached ‘Shopping’ related images the designer may use them on the website to provide a look & feel of retail if required – either separately or rotate in a single window

Target Market(s)

Retailers & Investors looking for retail space, Real Estate Brokers, Developers

Industry/Entity Type

Advertising

Number of Pages Required

3 page

Requirements
Must have
• Refer to existing site lotvantage.com -- all the existing functionalities are a must have.
Nice to have
• The Designer may use the retail related images on the website if required for making it more vibrant. Refer attached images Shopping(1-6).jpg

```html
<!DOCTYPE html>
<html lang="en">
<head>
<meta charset="utf-8">
<title>Lotvantage.com – Featured Projects</title>
<link href="https://fonts.googleapis.com/css2?family=Open+Sans:wght@400;600;700&display=swap" rel="stylesheet">
<style>
  :root {
    --ink: #2b2b2b;
    --muted: #6b6b6b;
    --accent: #f2a33a;
    --blue: #0a9cf2;
    --blue-dark: #0778c4;
    --tag-bg: rgba(45, 50, 60, 0.78);
    --band: #ebebeb;
    --line: #c9c9c9;
    --white: #ffffff;
  }
  * { box-sizing: border-box; margin: 0; padding: 0; }
  html, body { width: 1200px; height: 989px; overflow: hidden; background: var(--white); }
  body { font-family: "Open Sans", Arial, sans-serif; color: var(--ink); position: relative; }

  .section-title { font-size: 25px; font-weight: 600; position: relative; line-height: 1; }
  .section-title .hl { color: var(--accent); }
  .section-title::after {
    content: ""; position: absolute; left: 1px; bottom: -7px;
    width: 22px; height: 3px; background: var(--accent); border-radius: 2px;
  }

  .featured { position: absolute; left: 129px; top: 4px; width: 942px; }
  .featured-head { display: flex; align-items: center; gap: 17px; height: 28px; }
  .view-all {
    background: #333; color: var(--accent); font-size: 10px; font-weight: 700;
    padding: 2px 9px; border-radius: 4px; text-transform: uppercase; margin-top: 2px;
  }

  .project-row { display: flex; gap: 20px; margin-top: 32px; height: 271px; }
  .project-row + .divider { border-top: 1px dashed var(--line); margin-top: 17px; }
  .divider + .project-row { margin-top: 24px; }

  .project { width: 220px; display: flex; flex-direction: column; align-items: flex-start; }
  .project-photo {
    position: relative; width: 222px; height: 168px;
    border: 1px solid #e2e2e2; box-shadow: 1px 1px 2px rgba(0,0,0,.15);
  }
  .project-tag {
    position: absolute; right: 0; top: 15px; height: 21px;
    background: var(--tag-bg); color: var(--white);
    font-size: 11px; font-weight: 700; line-height: 21px; padding: 0 11px 0 14px;
  }
  .project-city { font-size: 19px; font-weight: 600; margin-top: 7px; line-height: 24px; }
  .project-address { font-size: 14px; color: var(--muted); line-height: 18px; font-weight: 600; }
  .listing-btn {
    margin-top: 14px; width: 148px; height: 35px; border-radius: 4px;
    background: var(--blue); border-bottom: 3px solid var(--blue-dark);
    color: var(--white); font-size: 14px; font-weight: 600; text-align: center; line-height: 33px;
    text-shadow: 0 1px 1px rgba(0,0,0,.25);
  }

  .mavens { position: absolute; left: 0; top: 736px; width: 1200px; height: 253px; background: var(--band); overflow: hidden; }
  .mavens-photo {
    position: absolute; left: 530px; top: 0; width: 670px; height: 253px;
    background:
      linear-gradient(90deg, var(--band) 0%, rgba(235,235,235,0) 22%),
      radial-gradient(circle at 40% 70%, #e6c93a 0 60px, transparent 62px),
      linear-gradient(90deg, #d8c9c0 0%, #c85a4a 25%, #e8d7b0 45%, #9aa6b6 70%, #6e7f9c 100%);
    opacity: .9;
  }
  .mavens-content { position: absolute; left: 130px; top: 36px; width: 560px; }
  .mavens p { font-size: 14px; line-height: 22px; margin-top: 29px; color: #222; }
  .mavens-form { margin-top: 17px; display: grid; grid-template-columns: 270px 270px; gap: 8px; margin-left: -1px; }
  .field {
    height: 37px; background: var(--white); border: 1px solid #d6d6d6; border-radius: 4px;
    font-size: 14px; color: #777; padding: 8px 12px;
  }
  .field.wide { grid-column: 1 / 3; height: 70px; }
</style>
</head>
<body>

<section class="featured">
  <div class="featured-head">
    <h2 class="section-title">Featured <span class="hl">Projects</span></h2>
    <span class="view-all">View All</span>
  </div>

  <div class="project-row">
    <article class="project">
      <div class="project-photo" role="img" aria-label="Shopping complex building exterior" style="background:linear-gradient(180deg,#cfe0ee 0%,#b9c8a8 45%,#8a9a88 80%,#a8a8a8 100%)"><span class="project-tag">Shopping Complex</span></div>
      <h3 class="project-city">Surat</h3>
      <p class="project-address">Corvella , Althan</p>
      <a class="listing-btn">VIEW THE LISTING</a>
    </article>
    <article class="project">
      <div class="project-photo" role="img" aria-label="High street retail building at dusk" style="background:linear-gradient(180deg,#2c3560 0%,#5a6a98 40%,#c8a070 70%,#3a3a40 100%)"><span class="project-tag">Shopping Complex</span></div>
      <h3 class="project-city">Faridabad</h3>
      <p class="project-address">Tarun 81 High Street , Sector-81</p>
      <a class="listing-btn">VIEW THE LISTING</a>
    </article>
    <article class="project">
      <div class="project-photo" role="img" aria-label="Glass-fronted shopping plaza" style="background:linear-gradient(180deg,#3a9ae0 0%,#9cc8ea 35%,#d8dde2 65%,#7aa070 100%)"><span class="project-tag">Shopping Complex</span></div>
      <h3 class="project-city">Gurgaon</h3>
      <p class="project-address">K7K Metroplaza , Sector-65</p>
      <a class="listing-btn">VIEW THE LISTING</a>
    </article>
    <article class="project">
      <div class="project-photo" role="img" aria-label="Tall retail tower against blue sky" style="background:linear-gradient(180deg,#1e3a78 0%,#4a78c0 55%,#9fb8de 100%)"><span class="project-tag">Retail Malls</span></div>
      <h3 class="project-city">Gurgaon</h3>
      <p class="project-address">Orin 24K , Sohna Road</p>
      <a class="listing-btn">VIEW THE LISTING</a>
    </article>
  </div>

  <div class="divider"></div>

  <div class="project-row">
    <article class="project">
      <div class="project-photo" role="img" aria-label="Mall exterior with forecourt" style="background:linear-gradient(180deg,#a8c4e6 0%,#cfdcea 35%,#8a7a80 65%,#b0a8a0 100%)"><span class="project-tag">Retail Malls</span></div>
      <h3 class="project-city">New Delhi</h3>
      <p class="project-address">Harbor Mall-Tagore Garden ,<br>Tagore Garden</p>
      <a class="listing-btn">VIEW THE LISTING</a>
    </article>
    <article class="project">
      <div class="project-photo" role="img" aria-label="Mall atrium with event stage" style="background:linear-gradient(180deg,#8a9ab0 0%,#d8dde6 45%,#6a7890 75%,#4a6aa0 100%)"><span class="project-tag">Retail Malls</span></div>
      <h3 class="project-city">Chennai</h3>
      <p class="project-address">ELMA Skybridge Mall , Aminjikarai</p>
      <a class="listing-btn">VIEW THE LISTING</a>
    </article>
    <article class="project">
      <div class="project-photo" role="img" aria-label="Mall interior with escalators" style="background:linear-gradient(180deg,#c8c0b8 0%,#ece8e4 50%,#8a8480 100%)"><span class="project-tag">Retail Malls</span></div>
      <h3 class="project-city">Chennai</h3>
      <p class="project-address">The Regal Mall , Velacheri</p>
      <a class="listing-btn">VIEW THE LISTING</a>
    </article>
    <article class="project">
      <div class="project-photo" role="img" aria-label="Blue glass mall facade" style="background:linear-gradient(180deg,#e8eef4 0%,#5a88c0 35%,#3a6aa8 70%,#8aa8c8 100%)"><span class="project-tag">Shopping Complex</span></div>
      <h3 class="project-city">Gurgaon</h3>
      <p class="project-address">RVN Arcadia 91 ,<br>Golf Course Road</p>
      <a class="listing-btn">VIEW THE LISTING</a>
    </article>
  </div>
</section>

<section class="mavens">
  <div class="mavens-photo" role="img" aria-label="Family shopping in a store with sale signs"></div>
  <div class="mavens-content">
    <h2 class="section-title">Lot <span class="hl">Mavens</span></h2>
    <p>Post your Retail Space requirement with us and our experts shall get back with suitable options and even help you in your transaction.<br>This is a F<strong>ree Service</strong>!</p>
    <form class="mavens-form">
      <div class="field">Enter your email address</div>
      <div class="field">Mobile</div>
      <div class="field wide">Add Description of Requirement</div>
    </form>
  </div>
</section>

</body>
</html>
```